Buss cards
Stationary & envelops
Buss cards - Transportation
Creative Brief
Simple
Harbor Crest Moving
412 West 57th Avenue Brooklyn, NY 11204
Info@Harborcrestmoving.example
www.harborcrestmoving.example
US DOT # 4718392
this is a moving company, that relocates household goods, any ideas you may have would be appreciated
Local & Long Distance Residential & Commercial Storage Facility visit us online: www.harborcrestmoving.example

```html
<!DOCTYPE html>
<html lang="en">
<head>
<meta charset="utf-8">
<title>Harbor Crest Moving — Business Cards</title>
<link href="https://fonts.googleapis.com/css2?family=Montserrat:wght@800&family=Open+Sans:wght@400;600&display=swap" rel="stylesheet">
<style>
  :root {
    --bg: #e4e6e9;
    --blue: #1f7ccc;
    --blue-deep: #1461a8;
    --blue-light: #4aa3e6;
    --ink: #3a3d42;
    --muted: #7a7f86;
    --white: #ffffff;
    --orange: #f07a22;
  }
  * { margin: 0; padding: 0; box-sizing: border-box; }
  html, body { width: 1200px; height: 797px; overflow: hidden; }
  body {
    background: var(--bg);
    font-family: "Open Sans", sans-serif;
    position: relative;
  }
  .card {
    position: absolute;
    top: 255px;
    width: 500px;
    height: 286px;
    border-radius: 22px;
    overflow: hidden;
    box-shadow: 0 4px 14px rgba(0,0,0,.12);
  }
  .card-back {
    left: 60px;
    background: linear-gradient(135deg, var(--blue-light) 0%, var(--blue) 45%, var(--blue-deep) 100%);
    color: var(--white);
    display: flex;
    flex-direction: column;
    align-items: center;
    justify-content: center;
    gap: 14px;
  }
  .card-front { left: 640px; background: var(--white); }
  .brand {
    font-family: "Montserrat", sans-serif;
    font-weight: 800;
    text-transform: uppercase;
    letter-spacing: .5px;
    display: flex;
    align-items: center;
    gap: 10px;
  }
  .brand-dot { width: 14px; height: 14px; border-radius: 50%; background: var(--orange); }
  .card-back .brand { font-size: 27px; color: var(--white); }
  .card-back .web { font-size: 12px; letter-spacing: .3px; opacity: .9; }
  .card-front .brand {
    position: absolute; top: 62px; left: 40px;
    font-size: 27px; color: var(--blue);
  }
  .wave { position: absolute; inset: 0; }
  .front-web {
    position: absolute; top: 26px; right: 26px;
    font-size: 10px; color: var(--muted);
  }
  .person { position: absolute; left: 36px; top: 176px; }
  .person-name { font-size: 16px; font-weight: 600; color: var(--ink); }
  .person-title { font-size: 10.5px; color: var(--muted); }
  .contact {
    position: absolute; left: 170px; top: 168px;
    list-style: none;
    font-size: 10px; color: var(--ink);
    line-height: 17px;
  }
  .contact li { display: flex; align-items: center; gap: 7px; }
  .contact svg { width: 10px; height: 10px; fill: var(--blue); flex: none; }
</style>
</head>
<body>

<section class="card card-back" aria-label="Card back">
  <div class="brand"><span class="brand-dot"></span>Harbor Crest Moving</div>
  <p class="web">www.harborcrestmoving.example</p>
</section>

<section class="card card-front" aria-label="Card front">
  <svg class="wave" viewBox="0 0 500 286" preserveAspectRatio="none" aria-hidden="true">
    <path d="M500 0 L500 286 L330 286 C390 240 400 170 440 110 C465 70 485 40 500 0 Z" fill="var(--blue)"/>
    <path d="M500 20 C470 90 430 140 400 200 C380 240 355 270 320 286" fill="none" stroke="var(--blue-light)" stroke-width="3"/>
    <path d="M500 45 C480 110 445 160 420 215 C405 248 385 272 360 286" fill="none" stroke="var(--white)" stroke-width="2"/>
  </svg>
  <p class="front-web">www.harborcrestmoving.example</p>
  <div class="brand"><span class="brand-dot"></span>Harbor Crest Moving</div>

  <div class="person">
    <p class="person-name">Dana Reyes</p>
    <p class="person-title">President</p>
  </div>

  <ul class="contact">
    <li><svg viewBox="0 0 10 10"><path d="M5 0C3 0 1.5 1.5 1.5 3.4 1.5 6 5 10 5 10S8.5 6 8.5 3.4C8.5 1.5 7 0 5 0Zm0 4.8A1.4 1.4 0 1 1 5 2a1.4 1.4 0 0 1 0 2.8Z"/></svg>412 West 57th Avenue</li>
    <li><svg viewBox="0 0 10 10"></svg>Brooklyn, NY 11204</li>
    <li><svg viewBox="0 0 10 10"><path d="M2 0 4 2.5 3 3.8C3.6 5 5 6.4 6.2 7L7.5 6 10 8 8.5 10C4 9.5.5 6 0 1.5Z"/></svg>1-800-555-0142</li>
    <li><svg viewBox="0 0 10 10"><path d="M2 0 4 2.5 3 3.8C3.6 5 5 6.4 6.2 7L7.5 6 10 8 8.5 10C4 9.5.5 6 0 1.5Z"/></svg>718-555-0176</li>
    <li><svg viewBox="0 0 10 10"><rect x="1" y="1" width="8" height="8" rx="1"/></svg>718-555-0193</li>
    <li><svg viewBox="0 0 10 10"><path d="M0 2h10v6H0Zm1 .8L5 5.5 9 2.8"/></svg>Info@Harborcrestmoving.example</li>
  </ul>
</section>

</body>
</html>
```